Business Card Design for DJ

Double-sided full colour business card, with containing the following key information:

DJ Marblequake
Phone (###) ###-####
Email: djmarblequake@pelnomail.net
Facebook: friendlinq.net/djmarblequake
Twitter: @djmarblequake

Bringing you the best in Top 40 - Retro - Funk

"It's gonna be a marblequake."

Club/Bar – Weddings – Private Parties - Corporate Events
3000W of portable sound
Dancefloor lighting with optional custom gobos
Available HD Projector and screen
Available custom video production
Free consultation

ORMB Licensed (small logo from http://www.ormb-rights.ca)
Member of TVSKE (small logo from http://www.tvske-guild.ca)

Requirements
Must have
• DJ Marblequake logo (attached) or alternative wordmark using type similar to CLUBLAND at http://tunevaultzone.net/uploads/posts/1226228091_6705615x.jpg
Nice to have
• headshot (attached), dance club look/feel

```html
<!DOCTYPE html>
<html lang="en">
<head>
<meta charset="utf-8">
<title>DJ Marblequake – Business Card</title>
<link rel="stylesheet" href="https://fonts.googleapis.com/css2?family=Jura:wght@500&family=Silkscreen:wght@700&display=swap">
<style>
  :root {
    --bg-dark: #1f1d19;
    --bg-mid: #2a2721;
    --wordmark: #f2f0ea;
    --tagline: #e9d51c;
    --accent-blue: #2cb8ec;
    --contact-text: #e6e6e6;
    --icon-fill: #d9d9d9;
    --icon-ring: #7a7a7a;
    --figure-dark: #0b0b0b;
    --figure-red: #b3161a;
  }
  html, body {
    margin: 0;
    padding: 0;
    overflow: hidden;
    background: var(--bg-dark);
  }
  .card {
    position: relative;
    width: 1200px;
    height: 678px;
    overflow: hidden;
    background: radial-gradient(ellipse at 50% 40%, var(--bg-mid) 0%, var(--bg-dark) 75%);
    font-family: "Jura", "Segoe UI", sans-serif;
    font-weight: 500;
  }
  .headshot {
    position: absolute;
    left: 0;
    top: 282px;
    width: 290px;
    height: 396px;
    border-radius: 46% 54% 0 0 / 26% 26% 0 0;
    background: linear-gradient(160deg, var(--figure-red) 0%, var(--figure-dark) 30%, var(--figure-dark) 100%);
    opacity: 0.95;
  }
  .wordmark {
    position: absolute;
    top: 108px;
    left: 0;
    width: 100%;
    text-align: center;
    color: var(--wordmark);
    font-size: 58px;
    letter-spacing: 3px;
    text-transform: uppercase;
    margin: 0;
    font-weight: 500;
  }
  .tagline {
    position: absolute;
    top: 286px;
    left: 0;
    width: 100%;
    text-align: center;
    color: var(--tagline);
    font-family: "Silkscreen", "Courier New", monospace;
    font-weight: 700;
    font-size: 30px;
    line-height: 44px;
    margin: 0;
    z-index: 1;
  }
  .genres {
    position: absolute;
    top: 378px;
    left: 0;
    width: 100%;
    text-align: center;
    color: var(--accent-blue);
    font-size: 31px;
    line-height: 43px;
    margin: 0;
  }
  .phone {
    position: absolute;
    top: 532px;
    left: 0;
    width: 100%;
    text-align: center;
    color: var(--accent-blue);
    font-size: 32px;
    letter-spacing: 1px;
    margin: 0;
  }
  .contact-row {
    position: absolute;
    left: 0;
    top: 618px;
    width: 100%;
    height: 36px;
    z-index: 1;
  }
  .contact {
    position: absolute;
    top: 0;
    display: flex;
    align-items: center;
    gap: 10px;
    color: var(--contact-text);
    font-size: 22px;
    white-space: nowrap;
  }
  .contact--email { left: 24px; }
  .contact--social { left: 450px; }
  .contact--handle { right: 30px; }
  .contact-icon {
    width: 34px;
    height: 34px;
    flex: none;
  }
  .plain-dot {
    width: 32px;
    height: 32px;
    border-radius: 50%;
    background: var(--icon-fill);
    flex: none;
  }
</style>
</head>
<body>
  <main class="card">
    <div class="headshot" role="img" aria-label="Stylised headshot of the DJ wearing headphones, black silhouette with red accents"></div>

    <h1 class="wordmark">DJ Marblequake</h1>

    <p class="tagline">It’s gonna be a Marblequake</p>

    <p class="genres">Bringing you the best in<br>Top 40 - Retro - Funk</p>

    <p class="phone">(###) ###-####</p>

    <div class="contact-row">
      <div class="contact contact--email">
        <svg class="contact-icon" viewBox="0 0 34 34" aria-hidden="true">
          <circle cx="17" cy="17" r="16" fill="var(--icon-fill)" stroke="var(--icon-ring)" stroke-width="1.5"/>
          <rect x="8" y="11" width="18" height="12" rx="1.5" fill="#ffffff" stroke="#555" stroke-width="1.2"/>
          <path d="M8.5 11.5 L17 18 L25.5 11.5" fill="none" stroke="#555" stroke-width="1.2"/>
        </svg>
        <span>djmarblequake@pelnomail.net</span>
      </div>

      <div class="contact contact--social">
        <span class="plain-dot" aria-hidden="true"></span>
        <span>friendlinq.net/djmarblequake</span>
      </div>

      <div class="contact contact--handle">
        <span class="plain-dot" aria-hidden="true"></span>
        <span>@djmarblequake</span>
      </div>
    </div>
  </main>
</body>
</html>
```